Business Card Design/Stationary Design

We would like designers to submit cool, hip business card designs (plus stationary designs) for a new, upstart software development company located in Toronto.
If you have any questions, please email us.
For inspiration on designs:
http://cardmuse.example/cool-business-cards/
http://layoutnotes.example/2008/05/36-cool-business-cards-you-should%E2%80%99ve-seen.html
http://gigharbor.example/general/18-smokin-hot-business-card-designs/

Card info:

Selvakumar (Selv) Nadarasan

Founder and CEO

47 Brindle Court, Suite 311

Toronto, ON M4K 2T8

Phone: 647-512-7730

Mobile: 416-273-5094

Fax: 647-512-7731

Email: selvakumar.nadarasan@mailbrook.example

www.quendrix.example
Updates

Hi everyone,

In terms of all the designs I have seen so far, here is what I like:

1.  I really like the "back" part of this design.  The "front" looks pretty decent as well, but for the "front", look at #2 on this list.  I like that.

http://www.pitchboard.example/image.aspx?imageLocation=1000_10001_2000_image.jpg&type=design300px&whiteLabelCustId=9999

2. "Side 1" of this I like, the front needs to be reworked.

http://www.pitchboard.example/image.aspx?imageLocation=1000_10002_2000_image.png&type=design300px&whiteLabelCustId=9999

3. http://www.pitchboard.example/image.aspx?imageLocation=1000_10003_2000_image.jpg&type=design300px&whiteLabelCustId=9999

4. http://www.pitchboard.example/image.aspx?imageLocation=1000_10004_2000_image.jpg&type=design300px&whiteLabelCustId=9999

Target Market(s)

We are focused on enterprise customers right now, so businesses with a long-term goal of also reaching out to the consumer market as well.

Industry/Entity Type

Software

Requirements
Must have
• Must look cool, ultra-modern, clean and eye-catching. Must incorporate our logo and the colors found in the logo.

```html
<!DOCTYPE html>
<html lang="en">
<head>
<meta charset="utf-8">
<title>Quendrix Letterhead</title>
<link rel="stylesheet" href="https://fonts.googleapis.com/css2?family=Arimo:wght@400;700&display=swap">
<style>
  :root {
    --canvas: #ffffff;
    --paper: #ffffff;
    --paper-edge: #9a9a9a;
    --brand-green: #8cc63e;
    --ink: #1f1f1f;
    --ink-soft: #3a3a3a;
  }
  html, body {
    margin: 0;
    padding: 0;
    width: 1200px;
    height: 1200px;
    overflow: hidden;
    background: var(--canvas);
    font-family: "Arimo", Arial, sans-serif;
    color: var(--ink);
  }
  .letterhead {
    position: absolute;
    left: 149px;
    top: 29px;
    width: 902px;
    height: 1147px;
    background: var(--paper);
    border: 2px solid var(--paper-edge);
    box-sizing: border-box;
  }
  .brand {
    position: absolute;
    left: 30px;
    top: 20px;
    height: 64px;
    display: flex;
    align-items: center;
    gap: 12px;
  }
  .brand-dot {
    width: 44px;
    height: 44px;
    border-radius: 50%;
    background: var(--brand-green);
  }
  .brand-name {
    font-size: 36px;
    font-weight: 400;
    color: var(--ink-soft);
    letter-spacing: 0.5px;
  }
  .sender {
    position: absolute;
    right: 28px;
    top: 26px;
    text-align: right;
    font-size: 13px;
    line-height: 16px;
  }
  .sender-name { font-weight: 700; }
  .sender-title { font-weight: 400; }
  .header-band {
    position: absolute;
    left: 0;
    right: 0;
    top: 84px;
    height: 24px;
    background: var(--brand-green);
  }
  .footer-band {
    position: absolute;
    left: 0;
    right: 0;
    bottom: 0;
    height: 58px;
    background: var(--brand-green);
    display: flex;
    flex-direction: column;
    align-items: center;
    justify-content: center;
    font-size: 11.5px;
    line-height: 15px;
    color: var(--ink);
  }
  .footer-row {
    display: flex;
    gap: 30px;
    font-weight: 700;
  }
  .footer-line { font-weight: 400; }
</style>
</head>
<body>
  <main class="letterhead">
    <div class="brand">
      <span class="brand-dot"></span>
      <span class="brand-name">Quendrix</span>
    </div>
    <div class="sender">
      <div class="sender-name">Selvakumar (Selv) Nadarasan</div>
      <div class="sender-title">Founder and CEO</div>
    </div>
    <div class="header-band"></div>
    <footer class="footer-band">
      <div class="footer-row">
        <span>47 Brindle Court, Suite 311</span>
        <span>Toronto, ON M4K 2T8</span>
        <span>Phone: 647-512-7730</span>
        <span>Mobile: 416-273-5094</span>
        <span>Fax: 647-512-7731</span>
      </div>
      <div class="footer-line">E-mail: selvakumar.nadarasan@mailbrook.example</div>
      <div class="footer-line">www.quendrix.example</div>
    </footer>
  </main>
</body>
</html>
```